Sophisticated, clean website reflecting my feminine, playful side to sell my abstract art,

I need a website no more than 3 pages to showcase my paintings, a little about me and some contact info. I do abstracts so looking for something a little edgy, yet feminine and current.
Updates

Hi there, These are some artists websites that I Iike: Mirabelvoss.com (I like how airy it is) tobiasmerrowind.com kevinplodderas.com (I like how it scrolls) I'll need a place for a photo ( a headshot-i do not have it yet so I'll need to be able to upload that later) as well as an area for my bio. Also, it's important that I will be able to upload any new photos and descriptions easily so it should be user friendly. Lastly, I like in a sunny place so would like to have this seem upbeat and playful as that is how i like to paint. thanks-I'm trying to upload my photos now -

Target Market(s)

ppl ages 35-70 who want large scale art for their homes

Industry/Entity Type

art

Coding

Coded - Design and coding required

Number of Pages Required

3 page

Colors

Designer to choose colors to be used in the design.

Requirements
Must have
• photos of my art, a place for my bio, be easy to reach me. tasteful-nothing too "in your face" -my clients are pretty high end and organized. They like clean lines
Nice to have
• sophisticated background, muted tones in the back-similar clean font throughout-no cursive
Should not have
• too many dark areas. Too many blocks of color. Too serious.

```html
<!DOCTYPE html>
<html lang="en">
<head>
<meta charset="utf-8">
<title>Marlowe Kessing Art</title>
<link href="https://fonts.googleapis.com/css2?family=Poppins:wght@400;500;600;700&family=Roboto:wght@300;400&display=swap" rel="stylesheet">
<style>
:root{
  --teal:#1b8a80;
  --teal-dark:#177a71;
  --navy:#3a4e9c;
  --accent:#e2533b;
  --ink:#1c1c1c;
  --text:#555;
  --bg-soft:#f4f4f5;
  --white:#fff;
}
*{margin:0;padding:0;box-sizing:border-box}
html,body{width:1200px;height:3202px;overflow:hidden}
body{position:relative;font-family:"Poppins",sans-serif;color:var(--ink);background:var(--white)}
.abs{position:absolute}

/* header */
.site-header{left:0;top:0;width:1200px;height:111px;background:var(--white);border-top:2px solid var(--teal)}
.logo{text-align:center;line-height:1}
.logo-main{display:block;font-weight:700;color:var(--teal);font-size:42px;letter-spacing:1px}
.logo-sub{display:block;font-weight:400;color:#333;font-size:18px;letter-spacing:4px;margin-top:6px}
.search{left:594px;top:12px;width:300px;height:46px;border:1px solid #999;border-radius:3px;font-family:"Roboto",sans-serif;font-size:14px;color:#333;padding:14px 16px}
.search svg{position:absolute;right:12px;top:12px}
.socials{display:flex;align-items:center;gap:9px;color:#444;font-size:16px}
.socials i{display:block;width:14px;height:14px;border-radius:50%;background:#333}
.main-nav{display:flex;gap:43px;font-size:15px;letter-spacing:1.5px;color:#333;align-items:center}
.main-nav .active{color:var(--accent);position:relative}
.main-nav .active::after{content:"";position:absolute;left:-2px;right:-2px;bottom:-12px;height:2px;background:var(--accent)}

/* hero */
.hero{left:0;top:111px;width:1200px;height:625px;background:linear-gradient(180deg,#2f3235 0%,#3a3d40 55%,#2a2c2e 100%)}
.hero-plant{left:0;top:190px;width:110px;height:340px;background:linear-gradient(160deg,#3f6a2e,#24401c);border-radius:0 60px 20px 0;opacity:.8}
.hero-sofa{left:210px;top:430px;width:780px;height:195px;background:linear-gradient(180deg,#2a2b2c,#1e1f20);border-radius:30px 30px 0 0}
.frame{top:58px;width:214px;height:280px;border:4px solid #111;box-shadow:0 10px 20px rgba(0,0,0,.5)}
.hero-title{left:0;top:420px;width:1200px;text-align:center;color:var(--white);font-weight:600;font-size:60px;letter-spacing:1px;line-height:1}
.hero-sub{left:230px;top:490px;width:740px;text-align:center;color:var(--white);font-weight:500;font-size:19px;line-height:29px}

/* about */
.about{left:0;top:736px;width:1200px;height:650px;background:linear-gradient(120deg,#f7f7f8 0%,#f1f1f3 60%,#eeeef1 100%)}
.about-dots{right:10px;top:20px;width:230px;height:200px;background-image:radial-gradient(#cfcfd3 1.5px,transparent 1.6px);background-size:13px 13px}
.about-dots2{left:0;top:540px;width:620px;height:110px;background-image:radial-gradient(#d3d3d7 1.5px,transparent 1.6px);background-size:13px 13px}
.photo-outline{left:377px;top:85px;width:210px;height:211px;border:3px solid var(--teal);border-radius:18px}
.photo-block{left:112px;top:350px;width:214px;height:214px;background:var(--teal);border-radius:18px}
.portrait{left:139px;top:112px;width:428px;height:428px;border-radius:16px;background:linear-gradient(180deg,#cfd7e8 0%,#b9a58e 45%,#6f86d0 100%)}
.eyebrow{font-size:16px;letter-spacing:3px;color:#333}
.section-title{font-weight:700;font-size:38px;letter-spacing:.5px;color:#111}
.about-text{left:649px;top:200px;width:440px;font-family:"Roboto",sans-serif;font-weight:300;font-size:14.6px;letter-spacing:-0.2px;line-height:33.5px;color:var(--text);text-align:justify}
.btn{display:flex;align-items:center;justify-content:center;border-radius:30px;background:var(--navy);color:var(--white);font-weight:600}
.btn-about{left:649px;top:486px;width:214px;height:46px;font-size:15px}

/* gallery */
.gallery{left:0;top:1386px;width:1200px;height:1084px;background:linear-gradient(180deg,#fafafa,#f6f6f6)}
.card{width:309px;height:385px;background:var(--white);box-shadow:0 2px 8px rgba(0,0,0,.12);border-radius:4px;text-align:center}
.card .art{position:absolute;left:9px;top:9px;width:291px;height:290px}
.card h3{position:absolute;left:0;top:316px;width:100%;font-weight:600;font-size:21px;color:#111}
.card p{position:absolute;left:0;top:350px;width:100%;font-weight:500;font-size:17px;color:#222}
.card.featured{background:var(--teal)}
.card.featured h3,.card.featured p{color:var(--white)}

/* contact */
.map{left:0;top:2470px;width:600px;height:543px;background:linear-gradient(135deg,#ececec,#e2e2e2)}
.map-pin{left:306px;top:232px}
.contact{left:600px;top:2470px;width:600px;height:543px;background:var(--teal);color:var(--white)}
.contact .eyebrow{color:var(--white);display:flex;align-items:center;gap:10px}
.contact .eyebrow::after{content:"";width:52px;height:1px;background:var(--white)}
.contact-line{font-family:"Roboto",sans-serif;font-size:23px;display:flex;gap:10px;align-items:flex-start}
.btn-dir{left:131px;top:273px;width:255px;height:54px;font-size:21px}

/* footer */
.site-footer{left:0;top:3013px;width:1200px;height:189px;background:#f5f5f6}
.footer-nav{display:flex;gap:44px;font-size:15px;font-weight:600;letter-spacing:2px;color:#111}
.footer-rule{left:111px;top:133px;width:977px;height:1px;background:#d8d8d8}
.copyright{left:0;top:150px;width:1200px;text-align:center;font-family:"Roboto",sans-serif;font-size:15px;color:#222}
</style>
</head>
<body>

<header class="site-header abs">
  <div class="logo abs" style="left:110px;top:18px;width:220px">
    <span class="logo-main">MARLOWE</span>
    <span class="logo-sub">KESSING ART</span>
  </div>
  <div class="search abs">Search
    <svg width="20" height="20" viewBox="0 0 20 20" fill="none" stroke="#333" stroke-width="1.6"><circle cx="8.5" cy="8.5" r="6.5"/><line x1="13.5" y1="13.5" x2="18.5" y2="18.5"/></svg>
  </div>
  <div class="socials abs" style="left:919px;top:27px"><i></i>|<i></i>|<i></i>|<i></i>|<i></i></div>
  <nav class="main-nav abs" style="left:401px;top:76px">
    <span class="active">HOME</span><span>ABOUT</span><span>ART GALLERY</span><span>CONTACT US</span>
    <span style="display:flex;align-items:center;gap:6px;margin-left:-4px">
      <svg width="13" height="13" viewBox="0 0 24 24" fill="#333"><path d="M6.6 10.8a15.1 15.1 0 0 0 6.6 6.6l2.2-2.2c.3-.3.7-.4 1-.2 1.1.4 2.3.6 3.6.6.6 0 1 .4 1 1V20c0 .6-.4 1-1 1A17 17 0 0 1 3 4c0-.6.4-1 1-1h3.5c.6 0 1 .4 1 1 0 1.3.2 2.5.6 3.6.1.3 0 .7-.2 1z"/></svg>
      +1 (555) 014 2290</span>
  </nav>
</header>

<section class="hero abs">
  <div class="hero-plant abs" role="img" aria-label="Potted plant leaves"></div>
  <div class="hero-sofa abs" role="img" aria-label="Dark sofa with throw blanket"></div>
  <div class="frame abs" style="left:249px;background:linear-gradient(135deg,#d9a32a,#b8461e 50%,#2e5d8a)" role="img" aria-label="Abstract painting in yellow, red and blue"></div>
  <div class="frame abs" style="left:481px;background:linear-gradient(180deg,#e6e2d8 0%,#e6e2d8 40%,#2f8fc0 55%,#cfdde6 100%)" role="img" aria-label="Abstract painting with blue drips"></div>
  <div class="frame abs" style="left:714px;background:linear-gradient(135deg,#e8ddd6,#c78a98 50%,#5b3a2c)" role="img" aria-label="Abstract floral painting in pink and brown"></div>
  <h1 class="hero-title abs">MARLOWE KESSING ART</h1>
  <p class="hero-sub abs">Sed ut perspiciatis unde omnis iste natus error sit voluptatem accusantium doloremque laudantium, totam rem</p>
  <svg class="abs" style="left:588px;top:572px" width="24" height="34" viewBox="0 0 24 34" fill="none" stroke="#fff" stroke-width="1.5"><line x1="12" y1="0" x2="12" y2="32"/><polyline points="2,22 12,32 22,22"/></svg>
</section>

<section class="about abs">
  <div class="about-dots abs"></div>
  <div class="about-dots2 abs"></div>
  <div class="photo-outline abs"></div>
  <div class="photo-block abs"></div>
  <div class="portrait abs" role="img" aria-label="Headshot of the artist"></div>
  <div class="eyebrow abs" style="left:649px;top:109px">ARTIST</div>
  <h2 class="section-title abs" style="left:649px;top:134px">ABOUT ME</h2>
  <p class="about-text abs">Sed ut perspiciatis unde omnis iste natus error sit voluptatem accusantium doloremque laudantium, totam rem aperiam, eaque ipsa quae ab illo inventore veritatis et quasi architecto beatae vitae dicta sunt explicabo. Nemo enim ipsam voluptatem quia voluptas sit aspernatur aut odit aut fugit, sed quia consequuntur magni dolores eos qui ratione voluptatem sequi nesciunt. Neque porro quisquam est, qui dolorem ipsum quia dolor sit amet, consectetur, adipisci velit, sed quia non numquam</p>
  <div class="btn btn-about abs">LEARN MORE ABOUT</div>
</section>

<section class="gallery abs">
  <div class="eyebrow abs" style="left:0;top:90px;width:1200px;text-align:center">ARTS</div>
  <h2 class="section-title abs" style="left:0;top:115px;width:1200px;text-align:center">ART GALLERY</h2>

  <div class="card abs" style="left:111px;top:190px"><div class="art" style="background:linear-gradient(135deg,#e7e2dc,#7d5aa0 50%,#ddd6d0)" role="img" aria-label="Painting Soft Static, purple blooms"></div><h3>SOFT STATIC</h3><p>40” X 40”</p></div>
  <div class="card featured abs" style="left:445px;top:190px"><div class="art" style="background:linear-gradient(135deg,#dfe6e3,#2a8b4a 45%,#2a2f38 60%,#dce4e0)" role="img" aria-label="Painting Calypso, green and black bursts"></div><h3>CALYPSO</h3><p>40” X 40”</p></div>
  <div class="card abs" style="left:778px;top:190px"><div class="art" style="background:linear-gradient(135deg,#d9a32a,#c7541e 45%,#2a5a8a 70%,#e0d7c0)" role="img" aria-label="Painting Golden Hour Glow, yellow and red swirls"></div><h3>GOLDEN HOUR GLOW</h3><p>40” X 40”</p></div>

  <div class="card abs" style="left:111px;top:601px"><div class="art" style="background:linear-gradient(180deg,#e6e2d8 0%,#e6e2d8 38%,#2f8fc0 45%,#d3e0e8 100%)" role="img" aria-label="Painting Tideline, blue drips"></div><h3>TIDELINE</h3><p>40” X 40”</p></div>
  <div class="card abs" style="left:445px;top:601px"><div class="art" style="background:linear-gradient(135deg,#e8ddd6,#b77a88 45%,#5b3a2c 80%)" role="img" aria-label="Painting Velvet Bloom, pink roses"></div><h3>VELVET BLOOM</h3><p>40” X 40”</p></div>
  <div class="card abs" style="left:778px;top:601px"><div class="art" style="background:linear-gradient(90deg,#8493ad 0%,#8e9bb3 30%,#e6e0d0 32%,#e6e0d0 52%,#12897c 54%,#0f6e66 100%)" role="img" aria-label="Painting Breaking Horizons, grey, cream and teal bands"></div><h3>BREAKING HORIZONS</h3><p>30” X 40”</p></div>
</section>

<div class="map abs" role="img" aria-label="Street map showing the studio location">
  <svg class="map-pin abs" width="22" height="30" viewBox="0 0 22 30"><path d="M11 0C5 0 0 5 0 11c0 8 11 19 11 19s11-11 11-19C22 5 17 0 11 0z" fill="#d0213b"/><circle cx="11" cy="11" r="4" fill="#fff"/></svg>
</div>

<section class="contact abs">
  <div class="eyebrow abs" style="left:95px;top:92px">GET IN TOUCH</div>
  <h2 class="section-title abs" style="left:95px;top:118px;color:#fff">CONTACT US</h2>
  <div class="contact-line abs" style="left:103px;top:182px;line-height:39px">
    <svg width="16" height="22" viewBox="0 0 22 30" style="margin-top:8px"><path d="M11 0C5 0 0 5 0 11c0 8 11 19 11 19s11-11 11-19C22 5 17 0 11 0z" fill="#fff"/><circle cx="11" cy="11" r="4" fill="#1b8a80"/></svg>
    <span>58 Linden Row Fairhaven<br>&nbsp;USA 30417</span>
  </div>
  <div class="btn btn-dir abs">GET DIRECTION</div>
  <div class="contact-line abs" style="left:103px;top:359px">
    <svg width="20" height="20" viewBox="0 0 24 24" fill="#fff" style="margin-top:4px"><path d="M6.6 10.8a15.1 15.1 0 0 0 6.6 6.6l2.2-2.2c.3-.3.7-.4 1-.2 1.1.4 2.3.6 3.6.6.6 0 1 .4 1 1V20c0 .6-.4 1-1 1A17 17 0 0 1 3 4c0-.6.4-1 1-1h3.5c.6 0 1 .4 1 1 0 1.3.2 2.5.6 3.6.1.3 0 .7-.2 1z"/></svg>
    <span>+1 (555) 014 2290</span>
  </div>
  <div class="contact-line abs" style="left:103px;top:425px">
    <svg width="24" height="18" viewBox="0 0 24 18" style="margin-top:6px"><rect width="24" height="18" rx="2" fill="#fff"/><polyline points="1,2 12,10 23,2" fill="none" stroke="#1b8a80" stroke-width="2"/></svg>
    <span>info@marlowekessingart.com</span>
  </div>
</section>

<footer class="site-footer abs">
  <div class="logo abs" style="left:110px;top:34px;width:220px">
    <span class="logo-main">MARLOWE</span>
    <span class="logo-sub">KESSING ART</span>
  </div>
  <nav class="footer-nav abs" style="left:389px;top:52px"><span>HOME</span><span>ABOUT</span><span>ART GALLERY</span><span>CONTACT US</span></nav>
  <div class="socials abs" style="left:921px;top:50px"><i></i>|<i></i>|<i></i>|<i></i>|<i></i></div>
  <div class="footer-rule abs"></div>
  <p class="copyright abs">©Copyright ©2022 Marlowe Kessing Art. All Rights Reserved.</p>
</footer>

</body>
</html>
```